Billboard Vexlor-Link Systems

Design of an A0 billboard (landscape, will be printed on adhesive foil) of our company with reference to the website (www.vexlor-link.net) and the activity through keywords / phrases such as Fastest data radio you can buy, data radio safe and independent , ...
Explanation: we set up radio networks for long-range data transmission, which work on our own frequencies and are therefore independent of the provider. The systems are used for water and energy supply systems, sewage systems, environmental measurement networks, ...

Industry/Entity Type

Water-, Energie- Distribution, Abwasser...

Requirements
Must have
• Logo, link on website
Nice to have
• Message
Should not have
• picture of our old product from present web. I will be discontinued shortly. Please use the new one I uploaded here.

```html
<!DOCTYPE html>
<html lang="en">
<head>
<meta charset="utf-8">
<title>Vexlor-Link Systems – Billboard Variants</title>
<link href="https://fonts.googleapis.com/css2?family=Open+Sans:wght@300;400;600;700;800&family=Saira+Condensed:wght@300;400&display=swap" rel="stylesheet">
<style>
  :root{
    --navy:#042f4c;
    --blue:#0a6aa8;
    --sky:#8fc0ea;
    --white:#ffffff;
    --ink:#000000;
    --sheet:#ffffff;
    --logo:#0b6cae;
    --panel-tint:#f3f5f7;
  }
  *{box-sizing:border-box;margin:0;padding:0}
  html,body{width:1200px;height:1167px;overflow:hidden;background:var(--sheet)}
  body{position:relative;font-family:"Open Sans",sans-serif}
  .board{position:absolute;overflow:hidden;box-shadow:0 4px 14px rgba(0,0,0,.28)}
  .board-bg{position:absolute;inset:0;width:100%;height:100%}
  .abs{position:absolute}
  .brand{position:absolute;font-family:"Open Sans",sans-serif;font-weight:700;color:var(--logo);white-space:nowrap}
  .headline{position:absolute;font-family:"Saira Condensed",sans-serif;color:var(--white);font-weight:400;line-height:1;white-space:nowrap}
  .headline .light{font-weight:300}
  .lead{position:absolute;color:var(--white);font-weight:300;line-height:1.25}
  .product{position:absolute;border-radius:6px;background:linear-gradient(180deg,#e2231a 0%,#c81d16 48%,#c9ced4 52%,#e6e9ec 75%,#d0201a 100%)}
  .tag{position:absolute;font-family:"Open Sans",sans-serif;font-weight:300;border-radius:4px;padding:0 6px;line-height:1.15;display:flex;align-items:center;white-space:nowrap}
  .tag-dark{background:var(--ink);color:var(--white);font-size:10.5px}
  .tag-light{background:var(--white);color:var(--ink);font-size:9px;font-weight:400}
  .url-bar{position:absolute;background:var(--navy);border-radius:6px;border-left:10px solid var(--blue);color:var(--white);font-weight:800;display:flex;align-items:center;justify-content:center;white-space:nowrap}
  .bullets{position:absolute;list-style:none;color:var(--white);font-weight:600;font-size:10px;line-height:1.1}
  .bullets li{position:relative;padding-left:12px}
  .bullets li::before{content:"";position:absolute;left:0;top:3px;width:4px;height:4px;border-radius:50%;background:var(--sky)}
  .url-plain{position:absolute;font-weight:600;white-space:nowrap}
</style>
</head>
<body>

<!-- Portrait board, top left -->
<section class="board board-portrait-a" style="left:17px;top:17px;width:457px;height:648px;background:var(--navy)">
  <svg class="board-bg" viewBox="0 0 457 648" preserveAspectRatio="none" aria-hidden="true">
    <path d="M0 0 H457 Q228 150 0 0Z" fill="var(--white)"/>
    <path d="M400 66 L457 40 V62Z" fill="var(--blue)" opacity=".6"/>
    <path d="M0 338 Q228 262 457 348 V378 Q228 282 0 350Z" fill="var(--blue)"/>
    <path d="M0 350 Q228 282 457 378 V648 H0Z" fill="var(--white)"/>
  </svg>
  <div class="brand" style="left:0;width:457px;text-align:center;top:45px;font-size:15px">Vexlor-Link Systems</div>
  <div class="headline" style="left:93px;top:98px;font-size:56px">Fastest data</div>
  <div class="headline" style="left:93px;top:152px;font-size:56px">radio <span class="light" style="font-size:44px">you can buy!</span></div>
  <p class="lead" style="left:78px;width:300px;top:229px;font-size:10px;text-align:center">we set up radio networks for long-range data transmission, which work on our own frequencies and are therefore independent of the provider.</p>
  <div class="product" role="img" aria-label="Photo of the new red data radio router units" style="left:117px;top:280px;width:195px;height:153px"></div>
  <div class="tag tag-dark" style="left:88px;top:460px;width:112px;height:22px">Water supply system</div>
  <div class="tag tag-dark" style="left:217px;top:459px;width:134px;height:35px">environmental<br>measurement networks</div>
  <div class="tag tag-dark" style="left:88px;top:486px;width:123px;height:22px">Energy supply systems</div>
  <div class="tag tag-dark" style="left:218px;top:498px;width:93px;height:22px">Sewage systems</div>
  <div class="url-bar" style="left:59px;top:541px;width:337px;height:49px;font-size:24px">www.vexlor-link.net</div>
</section>

<!-- Landscape board, top right -->
<section class="board board-landscape-a" style="left:497px;top:17px;width:668px;height:469px;background:var(--white)">
  <svg class="board-bg" viewBox="0 0 668 469" preserveAspectRatio="none" aria-hidden="true">
    <path d="M0 0 H366 L397 330 L360 469 H0Z" fill="var(--navy)"/>
    <path d="M366 0 H380 L422 330 L397 469 H380 L410 330Z" fill="var(--sky)"/>
    <path d="M0 366 H378 L360 469 H0Z" fill="var(--blue)"/>
    <path d="M420 0 H668 V66 H432Z" fill="var(--panel-tint)"/>
    <path d="M10 0 H65 L55 45Z" fill="var(--blue)" opacity=".55"/>
  </svg>
  <div class="brand" style="left:458px;width:210px;text-align:center;top:30px;font-size:15px">Vexlor-Link Systems</div>
  <div class="headline" style="left:82px;top:82px;font-size:66px">Fastest</div>
  <div class="headline" style="left:82px;top:132px;font-size:66px">Data radio</div>
  <div class="headline light" style="left:82px;top:186px;font-size:52px">you can buy!</div>
  <ul class="bullets" style="left:65px;top:281px;width:170px">
    <li>Sewage systems</li>
    <li style="margin-top:11px">environmental measurement networks</li>
  </ul>
  <ul class="bullets" style="left:237px;top:281px;width:150px">
    <li>Water supply system</li>
    <li style="margin-top:11px">Energy supply systems</li>
  </ul>
  <p class="lead" style="left:37px;width:330px;top:393px;font-size:11px;font-weight:400">We set up radio networks for long-range data transmission, which work on our own frequencies and are therefore independent of the provider.</p>
  <div class="product" role="img" aria-label="Photo of the new red data radio router units" style="left:400px;top:140px;width:235px;height:186px"></div>
  <div class="abs" style="left:463px;top:363px;width:159px;height:2px;background:var(--blue)"></div>
  <div class="url-plain" style="left:445px;width:170px;text-align:center;top:400px;font-size:20px;color:var(--navy)">www.vexlor-link.net</div>
</section>

<!-- Landscape board, bottom left -->
<section class="board board-landscape-b" style="left:17px;top:685px;width:668px;height:470px;background:var(--navy)">
  <svg class="board-bg" viewBox="0 0 668 470" preserveAspectRatio="none" aria-hidden="true">
    <path d="M490 0 H560 C420 100 350 300 355 470 H338 C332 300 378 100 490 0Z" fill="var(--blue)"/>
    <path d="M560 0 H668 V470 H355 C350 300 420 100 560 0Z" fill="var(--white)"/>
    <path d="M78 0 H150 L142 75Z" fill="var(--blue)" opacity=".45"/>
  </svg>
  <div class="brand" style="right:22px;top:60px;font-size:14px">Vexlor-Link Systems</div>
  <div class="headline" style="left:44px;top:143px;font-size:56px">Fastest data</div>
  <div class="headline" style="left:44px;top:196px;font-size:56px">radio <span class="light" style="font-size:44px">you can buy!</span></div>
  <p class="lead" style="left:47px;width:275px;top:276px;font-size:10px">we set up radio networks for long-range data transmission, which work on our own frequencies and are therefore independent of the provider.</p>
  <div class="tag tag-light" style="left:44px;top:348px;width:101px;height:20px">Water supply system</div>
  <div class="tag tag-light" style="left:44px;top:371px;width:110px;height:20px">Energy supply</div>
  <div class="tag tag-light" style="left:160px;top:348px;width:119px;height:31px">environmental<br>measurement networks</div>
  <div class="tag tag-light" style="left:161px;top:383px;width:83px;height:20px">Sewage systems</div>
  <div class="product" role="img" aria-label="Photo of the new red data radio router units" style="left:399px;top:166px;width:196px;height:159px"></div>
  <div class="url-bar" style="left:347px;top:359px;width:330px;height:49px;font-size:26px;border-radius:6px 0 0 6px">www.vexlor-link.net</div>
</section>

<!-- Portrait board, bottom right -->
<section class="board board-portrait-b" style="left:711px;top:505px;width:457px;height:649px;background:var(--white)">
  <svg class="board-bg" viewBox="0 0 457 649" preserveAspectRatio="none" aria-hidden="true">
    <path d="M215 290 L457 258 V300Z" fill="var(--sky)"/>
    <path d="M0 294 L457 280 V649 H0Z" fill="var(--navy)"/>
    <path d="M0 296 H55 C25 320 8 350 0 370Z" fill="var(--blue)" opacity=".5"/>
    <path d="M215 0 H457 V64 H228Z" fill="var(--panel-tint)"/>
    <rect x="0" y="546" width="457" height="62" fill="var(--blue)"/>
  </svg>
  <div class="brand" style="left:242px;width:215px;text-align:center;top:24px;font-size:15px">Vexlor-Link Systems</div>
  <div class="product" role="img" aria-label="Photo of the new red data radio router units" style="left:58px;top:70px;width:266px;height:208px"></div>
  <div class="headline" style="left:101px;top:314px;font-size:56px">Fastest data</div>
  <div class="headline" style="left:101px;top:367px;font-size:56px">radio <span class="light" style="font-size:44px">you can buy!</span></div>
  <div class="tag tag-light" style="left:117px;top:457px;width:97px;height:20px">Water supply system</div>
  <div class="tag tag-light" style="left:117px;top:480px;width:107px;height:20px">Energy supply</div>
  <div class="tag tag-light" style="left:229px;top:457px;width:116px;height:31px">environmental<br>measurement networks</div>
  <div class="tag tag-light" style="left:230px;top:491px;width:82px;height:20px">Sewage systems</div>
  <p class="lead" style="left:60px;width:337px;top:553px;font-size:10.5px;font-weight:400;text-align:center">We set up radio networks for long-range data transmission, which work on our own frequencies and are therefore independent of the provider.</p>
  <div class="url-plain" style="left:0;width:457px;text-align:center;top:616px;font-size:18px;font-weight:400;color:var(--white)">www.vexlor-link.net</div>
</section>

</body>
</html>
```